Industrial Professional Business Card Design (Vantrel Systems)

Would like professional looking business cards. Not too busy leaning towards minimal. Should have a slogan like:
"Industrial Automation and Control".

We are a tech company that programs industrial PLC computers. We also develop custom hardware solutions. Please use the logo for inspiration.

Target Market(s)

Mining, industrial, processing, automation, factory

Industry/Entity Type

Engineering

Contact Information for Business Card

Name, phone, email, website. job title.

Font styles to use
Other font styles liked:
• droid sans

Requirements
Must have
• Use colours that go well with the logo. Not too busy design.

```html
<!DOCTYPE html>
<html lang="en">
<head>
<meta charset="utf-8">
<title>Vantrel Systems — Business Card</title>
<link href="https://fonts.googleapis.com/css2?family=Noto+Sans:wght@400;500&family=Yellowtail&display=swap" rel="stylesheet">
<style>
  :root {
    --backdrop: #e2e2e2;
    --navy: #1f4a73;
    --navy-deep: #1a4069;
    --navy-light: #2a5a86;
    --orange: #ef6623;
    --ink: #1d2a38;
    --paper: #ffffff;
  }
  * { margin: 0; padding: 0; box-sizing: border-box; }
  html, body { width: 1200px; height: 1200px; overflow: hidden; }
  body {
    background: var(--backdrop);
    font-family: "Noto Sans", sans-serif;
    position: relative;
  }
  .card {
    position: absolute;
    left: 278px;
    width: 644px;
    height: 368px;
    overflow: hidden;
  }
  .card-front { top: 196px; background: var(--navy); }
  .card-back { top: 672px; background: var(--paper); }

  .machinery-backdrop {
    position: absolute; inset: 0;
    background:
      radial-gradient(circle at 88% 38%, var(--navy-light) 0%, rgba(42,90,134,0) 42%),
      radial-gradient(circle at 62% 8%, rgba(42,90,134,0.8) 0%, rgba(42,90,134,0) 30%),
      linear-gradient(135deg, var(--navy-deep), var(--navy));
  }
  .slogan {
    position: absolute; left: 0; right: 0; top: 150px;
    text-align: center;
    font-family: "Yellowtail", cursive;
    font-size: 46px;
    color: var(--paper);
    letter-spacing: -0.5px;
  }

  .corner-navy, .corner-orange { position: absolute; border-radius: 50%; }
  .corner-navy { width: 116px; height: 116px; right: -58px; top: -58px; background: var(--navy); }
  .corner-orange { width: 122px; height: 122px; left: -61px; bottom: -61px; background: var(--orange); }

  .brand {
    position: absolute; left: 48px; top: 196px;
    display: flex; align-items: center; gap: 10px;
  }
  .brand-dot { width: 18px; height: 18px; border-radius: 50%; background: var(--orange); }
  .brand-name { font-size: 31px; font-weight: 400; color: var(--navy); letter-spacing: -0.5px; }

  .job-title {
    position: absolute; left: 360px; top: 56px;
    font-size: 33px; color: var(--navy); font-weight: 400;
  }
  .contact-list { position: absolute; left: 372px; top: 138px; list-style: none; color: var(--ink); }
  .contact-item { display: flex; align-items: flex-start; gap: 6px; font-size: 17px; line-height: 22px; margin-bottom: 10px; }
  .contact-item.phone { font-size: 22px; line-height: 28px; }
  .contact-icon { width: 18px; height: 18px; flex: none; margin-top: 2px; }
  .phone .contact-icon { margin-top: 4px; }
</style>
</head>
<body>
  <section class="card card-front">
    <div class="machinery-backdrop" role="img" aria-label="Faded navy-tinted photograph of industrial gears and machinery"></div>
    <p class="slogan">Industrial Automation and Control</p>
  </section>

  <section class="card card-back">
    <div class="corner-navy"></div>
    <div class="corner-orange"></div>

    <div class="brand">
      <span class="brand-dot"></span>
      <span class="brand-name">Vantrel Systems</span>
    </div>

    <h1 class="job-title">Job Title</h1>
    <ul class="contact-list">
      <li class="contact-item phone">
        <svg class="contact-icon" viewBox="0 0 24 24"><path d="M17 2c3 4 3 11-3 17-2 2-5 3-8 3l-1-3 4-2 2 2c3-2 5-5 6-8l-2-2 2-4z" fill="var(--navy)"/></svg>
        <span>0000000000</span>
      </li>
      <li class="contact-item">
        <svg class="contact-icon" viewBox="0 0 24 24" fill="none" stroke="var(--navy)" stroke-width="1.6"><circle cx="11" cy="11" r="9"/><ellipse cx="11" cy="11" rx="4" ry="9"/><path d="M2 11h18M4 6h14M4 16h14"/></svg>
        <span>www.companyweb.com</span>
      </li>
      <li class="contact-item">
        <svg class="contact-icon" viewBox="0 0 24 24" fill="none" stroke="var(--navy)" stroke-width="1.8"><rect x="3" y="9" width="18" height="12"/><path d="M3 9l9-6 9 6M3 21l7-6M21 21l-7-6M3 9l9 7 9-7"/></svg>
        <span>info@email.com</span>
      </li>
      <li class="contact-item">
        <svg class="contact-icon" viewBox="0 0 24 24"><path d="M12 2a6 6 0 0 0-6 6c0 5 6 11 6 11s6-6 6-11a6 6 0 0 0-6-6z" fill="var(--navy)"/><circle cx="12" cy="8" r="2.2" fill="#fff"/><ellipse cx="12" cy="21" rx="7" ry="2" fill="none" stroke="var(--navy)" stroke-width="1.4"/></svg>
        <span>Company Name<br>Address 1,<br>Address 2.</span>
      </li>
    </ul>
  </section>
</body>
</html>
```